TAVRO Capital Group LLC a High Risk Big Rewards company for Rich Young Entrepreneurs

We would like a very modern, powerful in the eyes of our customers, modern, minimalist feel, financial gain. this business card is for young Rich entrepreneurs who want to invest money into High Risk, Big Rewards Businesses. The card Should sell the business!! let your creativity go Wild! I pick most of the designers for this project because of your BOLD Designs, I would like this card to be Bold, Modern, Minimalist, use as many effects in your graphic Artist Mind, Do not let the Financial sound of this business to make you think Conservative that's the last thing we are! if you have a lot of money and you want to play a risky market call US
Updates

Project Deadline Extended
Reason: have not received, enough designs to choose 1st and second place, sure I have received over 100 designs but it seems most designers are submitting every card they have ever made before and calling it mine, please we are looking for fresh ideas please!

Target Market(s)

Private Risky Investors

Industry/Entity Type

Financial

Contact Information for Business Card

powerful in the eyes of our customers,modern, minimalist feel

Font styles to use
Other font styles liked:
• Modern feeling fonts

Requirements
Must have
• The Company Name is TAVRO Capital Group LLC and it must be on the CARD
• My Name, title, Cell , email
• Delvin Ashcroft G.E.D.
• Managing Member
• 555.038.6195
• delvin@tavrocapitalgroup.example
Nice to have
• try a black thick plastic card with round corners with Delvin Ashcroft GED (make sure GED is smaller than name) just on one side of the card, and my phone number with out the icons and email on the other side, this card should look like a exclusive credit card or exclusive VIP card, something you would never loose

```html
<!DOCTYPE html>
<html lang="en">
<head>
<meta charset="utf-8">
<title>TAVRO Capital Group LLC – Business Card</title>
<link rel="stylesheet" href="https://fonts.googleapis.com/css2?family=Montserrat:wght@400;500;700;800&display=swap">
<style>
  :root {
    --backdrop: #3a3a3c;
    --card-white: #ffffff;
    --brand-blue: #1a4fa3;
    --brand-blue-deep: #0d3178;
    --brand-blue-light: #2f6fd6;
    --ink-gray: #4a4a4a;
    --ink-soft: #5c5c5c;
    --on-blue: #ffffff;
  }
  * { box-sizing: border-box; margin: 0; padding: 0; }
  html, body { width: 1200px; height: 900px; overflow: hidden; }
  body {
    background: var(--backdrop);
    font-family: "Montserrat", Arial, sans-serif;
    display: flex;
    flex-direction: column;
    align-items: center;
    justify-content: center;
    gap: 60px;
  }
  .card {
    width: 560px;
    height: 320px;
    border-radius: 22px;
    position: relative;
    overflow: hidden;
    box-shadow: 0 10px 24px rgba(0,0,0,0.35);
  }

  /* Front side */
  .card--front {
    background: var(--card-white);
    display: flex;
    align-items: center;
    padding: 0 36px 0 34px;
  }
  .brand {
    width: 210px;
    display: flex;
    flex-direction: column;
    align-items: center;
    gap: 14px;
  }
  .brand__dot {
    width: 76px;
    height: 76px;
    border-radius: 50%;
    background: var(--brand-blue);
  }
  .brand__name {
    font-weight: 800;
    font-size: 21px;
    line-height: 1.05;
    text-transform: uppercase;
    color: var(--brand-blue);
    text-align: center;
    letter-spacing: 0.3px;
  }
  .divider {
    width: 2px;
    height: 150px;
    background: var(--brand-blue);
    margin: 0 22px 0 18px;
  }
  .contact { display: flex; flex-direction: column; }
  .contact__name {
    font-weight: 700;
    font-size: 19px;
    color: var(--brand-blue);
  }
  .contact__title {
    font-weight: 700;
    font-size: 13px;
    color: var(--ink-gray);
    margin-top: 4px;
    margin-bottom: 18px;
  }
  .contact__line {
    display: flex;
    align-items: center;
    gap: 9px;
    font-weight: 500;
    font-size: 12.5px;
    color: var(--ink-soft);
    margin-top: 6px;
  }
  .contact__icon { width: 13px; height: 13px; flex: none; }

  /* Back side */
  .card--back {
    background: radial-gradient(ellipse at 50% 50%, var(--brand-blue-light) 0%, var(--brand-blue) 45%, var(--brand-blue-deep) 100%);
    display: flex;
    align-items: center;
    justify-content: center;
    gap: 18px;
  }
  .card--back .brand__dot {
    width: 96px;
    height: 96px;
    background: var(--on-blue);
  }
  .card--back .brand__name {
    color: var(--on-blue);
    font-size: 28px;
    text-align: left;
  }
</style>
</head>
<body>

  <section class="card card--front" aria-label="Business card front">
    <div class="brand">
      <div class="brand__dot"></div>
      <div class="brand__name">TAVRO Capital<br>Group, LLC</div>
    </div>
    <div class="divider"></div>
    <div class="contact">
      <div class="contact__name">Delvin Ashcroft G.E.D.</div>
      <div class="contact__title">Managing Member</div>
      <div class="contact__line">
        <svg class="contact__icon" viewBox="0 0 24 24" aria-hidden="true">
          <path fill="#1a4fa3" d="M6.6 10.8a15.1 15.1 0 0 0 6.6 6.6l2.2-2.2a1 1 0 0 1 1-.25 11.4 11.4 0 0 0 3.6.57 1 1 0 0 1 1 1V20a1 1 0 0 1-1 1A17 17 0 0 1 3 4a1 1 0 0 1 1-1h3.5a1 1 0 0 1 1 1c0 1.25.2 2.45.57 3.6a1 1 0 0 1-.25 1z"/>
        </svg>
        <span>555.038.6195</span>
      </div>
      <div class="contact__line">
        <svg class="contact__icon" viewBox="0 0 24 24" aria-hidden="true">
          <rect x="2.5" y="5" width="19" height="14" rx="1.5" fill="none" stroke="#1a4fa3" stroke-width="2"/>
          <path d="M3 6l9 7 9-7" fill="none" stroke="#1a4fa3" stroke-width="2"/>
        </svg>
        <span>delvin@tavrocapitalgroup.example</span>
      </div>
    </div>
  </section>

  <section class="card card--back" aria-label="Business card back">
    <div class="brand__dot"></div>
    <div class="brand__name">TAVRO Capital<br>Group, LLC</div>
  </section>

</body>
</html>
```